Health Wellbeing Beauty online Shop

I have attached a full spec, however in summary this is a new business startup selling skincare products.

We need a web design for new wellbeing website, selling skincare products so need an eCommerce solution . On the home page I would like these faces to dissolve into each other on a loop or use a honeycomb style transation.
You will need the option of being able to log into an account, either through chatterbook, quorvix, tweedle or create an account. For created accounts, obviously need the facility to be able to reset passwords, see previous orders, track current order, and maintain favourites.
It should be PC, mobile and tablet friendly.

Look and Feel
It should be an elegant, modern, professional, trendy, unisex website. It should look clean and calm. Am happy to try interesting and slightly unusual designs. I would also like to have chat functionality, either powered by morvaLKtalk or by Quo 81.
Websites I like are
https://www.noble-radiance.example.co.uk/
https://www.onlyminerals.example.co.uk/
http://www.claramedica.example.com/

PLEASE DO USE YOUR KNOWELDGE OF WHAT WORKS FOR WEB DESIGN. YOU’RE THE EXPERT AND NEED YOUR EXPERTISE. CARTE BLANCHE TO DESIGN AS YOU SEE FIT. Please be creative, I need my site to stand out from the crowd.

Target Market(s)

Target Market
Middle aged women are our most common client, however, younger patients, both male and female, will often visit the site. In summary, I would like the site to appeal to all age brackets.

Requirements
Must have
• Need shop to be exactly like shop on this link http://www.claramedica.example.com/
Nice to have
• i would like something unique and creative

```html
<!DOCTYPE html>
<html lang="en">
<head>
<meta charset="utf-8">
<title>LM8 Skin Clinic</title>
<link href="https://fonts.googleapis.com/css2?family=Ubuntu:wght@400;500;700&family=PT+Sans:wght@400;700&display=swap" rel="stylesheet">
<style>
:root{
  --orange:#f26522;
  --orange-deep:#d9531e;
  --ink:#2b2f36;
  --dark:#2e2e30;
  --footer:#333335;
  --brown:#8a5a1e;
  --grey:#ebebeb;
  --line:#dcdcdc;
  --white:#fff;
  --text:#333;
}
*{box-sizing:border-box;margin:0;padding:0}
html,body{width:1200px;height:2163px;overflow:hidden;background:var(--white);font-family:"PT Sans",Arial,sans-serif;color:var(--text)}
.abs{position:absolute}
.head-font{font-family:"Ubuntu",Arial,sans-serif}

/* header */
.site-header{position:absolute;left:0;top:0;width:1200px;height:88px}
.brand{left:86px;top:22px;display:flex;align-items:center;gap:10px}
.brand-dot{width:40px;height:40px;border-radius:50%;border:2px solid var(--ink)}
.brand-name{font-family:"Ubuntu",sans-serif;font-weight:500;font-size:24px;color:var(--ink)}
.search{left:410px;top:25px;width:328px;height:40px;background:var(--grey);font-size:13px;font-style:italic;color:#777;padding:11px 12px}
.search-btn{left:676px;top:25px;width:62px;height:40px;background:#1d1d1d}
.login-social{left:746px;top:25px;width:202px;height:40px;background:#3b5b9b;color:#fff;font-size:14px;display:flex;align-items:center;justify-content:center}
.account{left:956px;top:22px;width:158px;height:44px;border:2px solid var(--line);font-size:13px;display:flex;align-items:center;gap:10px;padding-left:14px}
.nav{left:0;top:88px;width:1200px;height:46px;background:var(--ink);display:flex;align-items:center;padding-left:87px;gap:44px}
.nav a{color:#fff;font-size:12.5px;text-transform:uppercase;text-decoration:none;letter-spacing:.2px}

/* hero */
.hero{left:0;top:151px;width:1200px;height:404px;background:linear-gradient(90deg,#ecebea,#e4e3e2)}
.hero-title{left:92px;top:128px;font-family:"Ubuntu",sans-serif;font-weight:500;font-size:60px;color:var(--orange-deep);letter-spacing:1px}
.hero-text{left:95px;top:198px;width:480px;font-size:14px;line-height:21px;color:#333}
.hero-more{left:95px;top:248px;font-size:13px;font-weight:700;color:#333}
.hero-faces{left:649px;top:19px;width:458px;height:370px;background:radial-gradient(ellipse at center,#c99a82,#a77563 60%,#e4e3e2 100%);clip-path:polygon(25% 0,75% 0,100% 50%,75% 100%,25% 100%,0 50%)}
.hero-dots{left:578px;top:365px;display:flex;gap:6px}
.hero-dots span{width:9px;height:9px;border-radius:50%;background:#fff}
.hero-dots span:first-child{background:var(--orange)}

/* sidebar */
.panel-head{background:var(--ink);color:#fff;font-family:"Ubuntu",sans-serif;font-weight:500;font-size:18px;display:flex;align-items:center;justify-content:space-between;padding:0 12px}
.panel-list{background:var(--orange);padding:4px 4px}
.panel-list li{list-style:none;height:30px;border-bottom:1px solid rgba(255,255,255,.6);color:#fff;font-size:13px;display:flex;align-items:center;justify-content:space-between;padding:0 14px 0 28px}
.panel-list li:last-child{border-bottom:0}

/* products */
.section-title{font-family:"Ubuntu",sans-serif;font-weight:500;font-size:19px;color:#222}
.product{width:236px}
.product-frame{height:266px;border:2px solid var(--line);padding:8px}
.product-shot{width:100%;height:100%;background:radial-gradient(circle at 50% 55%,#d8d8d8,#f4f4f4 45%,#fff 70%)}
.product-name{font-size:16px;margin-top:10px}
.product-price{font-family:"Ubuntu",sans-serif;font-weight:700;font-size:20px;color:var(--orange-deep)}
.shop-btn{margin-top:6px;width:95px;height:36px;background:#8a4b14;color:#fff;font-size:12px;font-weight:700;display:flex;align-items:center;justify-content:center}

/* info tiles */
.tile{height:217px;color:#fff;text-align:center}
.tile h3{font-family:"Ubuntu",sans-serif;font-weight:500;font-size:24px;margin-top:26px}
.tile-about{background:linear-gradient(90deg,#f08a4b,#f7a060)}
.tile-about p{font-size:13px;line-height:18px;padding:6px 28px 0;text-align:justify;text-align-last:center}
.tile-hours{background:var(--orange)}
.tile-contact{background:linear-gradient(90deg,#e85a1a,#c95019)}
.field{margin:0 auto;width:284px;height:36px;background:#fbe2d4;color:#555;font-size:11px;text-align:left;padding:12px 14px}

/* reviews */
.reviews{left:0;top:1290px;width:1200px;height:354px;background:linear-gradient(90deg,#262628,#2e2e30 50%,#29292b);color:#fff;text-align:center}
.reviews h2{font-family:"Ubuntu",sans-serif;font-weight:500;font-size:26px;margin-top:30px}
.reviews p{width:620px;margin:14px auto 0;font-size:13.5px;line-height:21px}
.avatar{left:542px;top:155px;width:116px;height:116px;border-radius:50%;border:3px solid #fff;background:linear-gradient(#6b4a3e,#c59684)}

/* newsletter */
.newsletter{left:0;top:1644px;width:1200px;height:161px;background:var(--brown)}
.newsletter h2{left:87px;top:30px;color:#fff;font-family:"Ubuntu",sans-serif;font-weight:500;font-size:25px}
.nl-input{left:87px;top:80px;width:721px;height:44px;background:#fff;font-size:12px;font-style:italic;color:#555;padding:15px 12px}
.nl-btn{left:902px;top:80px;width:212px;height:44px;background:#fff;color:#222;font-size:15px;font-weight:700;letter-spacing:.5px;display:flex;align-items:center;justify-content:center}

/* footer */
.footer{left:0;top:1805px;width:1200px;height:323px;background:var(--footer);color:#fff}
.footer h4{font-family:"Ubuntu",sans-serif;font-weight:500;font-size:19px;position:absolute;top:46px}
.foot-brand{left:140px;top:38px;display:flex;flex-direction:column;align-items:center;gap:8px}
.foot-brand .brand-dot{width:60px;height:60px;border-color:#b08a4a}
.foot-brand .brand-name{color:#b08a4a}
.contact-list{left:87px;top:174px;font-size:13px;line-height:26px}
.links{left:357px;top:100px;font-size:11.5px;line-height:28.5px;list-style:none}
.map{left:573px;top:103px;width:281px;height:173px;background:linear-gradient(135deg,#d8d4cc,#c9c4b8 50%,#ddd8cf)}
.socials{left:931px;top:104px;display:flex;gap:7px}
.socials span{width:31px;height:31px;border-radius:50%;border:2px solid #ddd}
.copyright{left:0;top:2128px;width:1200px;height:35px;background:#222;color:#bbb;font-size:11px;display:flex;align-items:center;justify-content:center}
</style>
</head>
<body>

<header class="site-header">
  <div class="abs brand"><span class="brand-dot"></span><span class="brand-name">LM8</span></div>
  <div class="abs search">Search...</div>
  <div class="abs search-btn">
    <svg width="62" height="40" viewBox="0 0 62 40"><circle cx="29" cy="18" r="6" fill="none" stroke="#fff" stroke-width="2.5"/><line x1="33" y1="23" x2="37" y2="27" stroke="#fff" stroke-width="2.5"/></svg>
  </div>
  <div class="abs login-social">Login with chatterbook</div>
  <div class="abs account">
    <svg width="24" height="20" viewBox="0 0 24 20"><path d="M2 6h20l-3 11H5z" fill="none" stroke="#333" stroke-width="2"/><circle cx="19" cy="4" r="4" fill="#222"/></svg>
    Create an account
  </div>
</header>

<nav class="abs nav">
  <a>Home</a><a>Skin lightening tablets</a><a>Skin lighteningb creams</a><a>Skin lightening soaps</a><a>Skin lightening vials</a><a>Contact</a><a>About us</a>
</nav>

<section class="abs hero">
  <h1 class="abs hero-title">LM8 SKIN CLINIC</h1>
  <p class="abs hero-text">We need a web design for new wellbeing website. At the moment, I would like to focus on selling</p>
  <a class="abs hero-more">READ MORE &gt;&gt;</a>
  <div class="abs hero-faces" role="img" aria-label="Honeycomb of client portrait photographs"></div>
  <div class="abs hero-dots"><span></span><span></span><span></span></div>
</section>

<aside class="abs" style="left:87px;top:583px;width:248px">
  <div class="panel-head" style="height:49px">REFINE BY <span>&#10140;</span></div>
  <ul class="panel-list">
    <li>Name<span>&rsaquo;</span></li><li>Top Sellers<span>&rsaquo;</span></li><li>Highest review score<span>&rsaquo;</span></li><li>Price high to low<span>&rsaquo;</span></li><li>Price low to high<span>&rsaquo;</span></li>
  </ul>
  <div class="panel-head" style="height:49px;margin-top:8px">CATEGORIES <span>&#10140;</span></div>
  <ul class="panel-list">
    <li>Sun lightening Creams<span>&rsaquo;</span></li><li>Sun lightening Tablets<span>&rsaquo;</span></li><li>Sun lightening Soaps<span>&rsaquo;</span></li><li>Sun lightening Vials<span>&rsaquo;</span></li><li>Sun lightening Systems<span>&rsaquo;</span></li>
  </ul>
</aside>

<h2 class="abs section-title" style="left:360px;top:580px">OUR PRODUCTS</h2>
<svg class="abs" style="left:1044px;top:580px" width="52" height="22" viewBox="0 0 52 22">
  <circle cx="11" cy="11" r="10" fill="#222"/><path d="M13 6l-5 5 5 5" stroke="#fff" stroke-width="2.5" fill="none"/>
  <circle cx="39" cy="11" r="10" fill="#222"/><path d="M37 6l5 5-5 5" stroke="#fff" stroke-width="2.5" fill="none"/>
</svg>

<div class="abs product" style="left:360px;top:626px">
  <div class="product-frame"><div class="product-shot" role="img" aria-label="Cream jar product photo"></div></div>
  <div class="product-name">Sun lightening creams</div><div class="product-price">£189.90</div><div class="shop-btn">SHOP NOW</div>
</div>
<div class="abs product" style="left:620px;top:626px">
  <div class="product-frame"><div class="product-shot" role="img" aria-label="Cream jar product photo"></div></div>
  <div class="product-name">Sun lightening creams</div><div class="product-price">£189.90</div><div class="shop-btn">SHOP NOW</div>
</div>
<div class="abs product" style="left:878px;top:626px">
  <div class="product-frame"><div class="product-shot" role="img" aria-label="Cream jar product photo"></div></div>
  <div class="product-name">Sun lightening creams</div><div class="product-price">£189.90</div><div class="shop-btn">SHOP NOW</div>
</div>

<div class="abs tile tile-about" style="left:88px;top:1019px;width:324px" role="img" aria-label="About us panel over a soft-toned portrait photograph">
  <h3>ABOUT US</h3>
  <p>Lorem ipsum dolor sit amet, consectetur adipiscing elit. Phasellus non sodales ipsum. Pellentesquac nisi eu sem suscipit luctus. Duis commodo aliquam mi, non pellentesque est finibus vitae.</p>
  <p style="font-weight:700;margin-top:6px">READ MORE &gt;&gt;</p>
</div>

<div class="abs tile tile-hours" style="left:438px;top:1019px;width:325px">
  <h3>AVAILABILITY</h3>
  <div style="display:flex;align-items:center;gap:12px;margin:22px 0 0 32px;font-size:12.5px">
    <svg width="30" height="30" viewBox="0 0 30 30"><circle cx="15" cy="15" r="13" fill="none" stroke="#fff" stroke-width="2.5"/><path d="M15 8v7h6" stroke="#fff" stroke-width="2.5" fill="none"/></svg>
    MONDAY - FRIDAY : &nbsp;&nbsp;8AM - 18:00PM
  </div>
  <div style="display:flex;align-items:center;gap:12px;margin:18px 0 0 32px;font-size:12.5px;text-align:left">
    <svg width="30" height="30" viewBox="0 0 30 30"><rect width="30" height="30" rx="6" fill="#fff"/><path d="M9 7c-2 2 0 8 5 12s9 5 10 3l-3-4-3 2c-2-1-4-3-5-5l2-3z" fill="var(--orange)"/></svg>
    <span>+44 800 612 4470<br>Answerphone out of hours</span>
  </div>
</div>

<div class="abs tile tile-contact" style="left:787px;top:1019px;width:326px" role="img" aria-label="Contact form panel over a warm portrait photograph">
  <h3>GET IN TOUCH</h3>
  <div class="field" style="margin-top:14px">Name</div>
  <div class="field" style="margin-top:8px">Email address</div>
  <div style="margin:8px 0 0 21px;width:88px;height:36px;background:#f7c8ad;color:#d9531e;font-size:13px;display:flex;align-items:center;justify-content:center;gap:6px">&#10148; SEND</div>
</div>

<section class="abs reviews">
  <h2>OUR CLIENTS REVIEW</h2>
  <p>Morbi a euismod sapien, ac porttitor sem. Suspendisse molestie at urna quis accumsan. Suspendisse potenti. Integer id dui elementum, feugiat erat quis, ultricies dolor.Morbi a euismod sapien, ac porttitor sem. Suspendisse molestie at urna quis accumsan. Suspendisse</p>
  <svg class="abs" style="left:438px;top:198px" width330" height="24" viewBox="0 0 330 24" width="330">
    <path d="M14 2l-10 10 10 10" stroke="#fff" stroke-width="3.5" fill="none"/>
    <path d="M316 2l10 10-10 10" stroke="#fff" stroke-width="3.5" fill="none"/>
  </svg>
  <div class="abs avatar" role="img" aria-label="Client portrait photograph"></div>
  <div class="abs" style="left:0;top:282px;width:1200px;font-size:17px">Porttitor</div>
  <div class="abs" style="left:0;top:305px;width:1200px;font-size:13px">Client</div>
</section>

<section class="abs newsletter">
  <h2 class="abs">SUBSCRIBE TO NEWSLETTER</h2>
  <div class="abs nl-input">Email address</div>
  <div class="abs nl-btn">SUBSCRIBE</div>
</section>

<footer class="abs footer">
  <div class="abs foot-brand"><span class="brand-dot"></span><span class="brand-name">LM8</span></div>
  <div class="abs contact-list">
    Calling from the UK<br>
    <span style="padding-left:28px">0800 612 4470</span><br>
    Calling from Overseas<br>
    <span style="padding-left:28px">+44 800 612 4470</span><br>
    <span style="padding-left:28px">www.lm8skincare.example.com</span>
  </div>
  <h4 style="left:357px">QUICK LINKS</h4>
  <ul class="abs links">
    <li>&#9656; Home</li><li>&#9656; Skin Lightening Tablets</li><li>&#9656; Skin Lightening Creams</li><li>&#9656; Skin Lightening Soaps</li><li>&#9656; Skin Lightening Vials</li><li>&#9656; Contact</li><li>&#9656; About Us</li>
  </ul>
  <h4 style="left:573px">OUR LOCATION</h4>
  <div class="abs map" role="img" aria-label="Street map showing the clinic location"></div>
  <h4 style="left:931px">FOLLOW US</h4>
  <div class="abs socials"><span></span><span></span><span></span><span></span><span></span></div>
</footer>

<div class="abs copyright">@copyright 2016 LM8 Skin care clinic.All Rights Reserved</div>

</body>
</html>
```